Modern Design Business Card industrial maintenance company

Business card design for Company named Brookvale Equipment Services

Target Market(s)

Industrial

Industry/Entity Type

Maintenance and repair

Contact Information for Business Card

Place holder for address, office phone, mobile number and email

Requirements
Must have
• Clean modern look
Nice to have
• N/a

```html
<!DOCTYPE html>
<html lang="en">
<head>
<meta charset="utf-8">
<title>Brookvale Equipment Services – Business Card</title>
<link rel="stylesheet" href="https://fonts.googleapis.com/css2?family=Montserrat:ital,wght@0,500;0,600;0,700;0,800;1,500&display=swap">
<style>
  :root {
    --backdrop: #e6e7e9;
    --card: #ffffff;
    --orange: #f68b1f;
    --ink: #111111;
    --ink-soft: #2b2b2b;
    --faint: #cfcfcf;
  }
  * { box-sizing: border-box; margin: 0; padding: 0; }
  html, body {
    width: 1200px; height: 1200px; overflow: hidden;
    background: var(--backdrop);
    font-family: "Montserrat", sans-serif;
    color: var(--ink);
  }
  .canvas { position: relative; width: 1200px; height: 1200px; }

  .card {
    position: absolute;
    left: 199px; width: 802px; height: 460px;
    background: var(--card);
    border-radius: 17px;
    overflow: hidden;
    box-shadow: 6px 8px 10px rgba(0,0,0,0.28);
  }
  .card--front { top: 133px; }
  .card--back { top: 626px; }

  .card__shapes { position: absolute; inset: 0; width: 100%; height: 100%; }

  /* brand block */
  .brand { position: absolute; display: flex; flex-direction: column; align-items: center; }
  .brand__mark {
    border: 4px solid var(--ink);
    border-radius: 50%;
  }
  .brand__name, .brand__tagline {
    font-weight: 700; color: var(--ink); text-transform: uppercase; white-space: nowrap;
  }
  .brand--front { left: 201px; width: 400px; top: 113px; }
  .brand--front .brand__mark { width: 108px; height: 108px; }
  .brand--front .brand__name { font-size: 31px; letter-spacing: 3px; margin-top: 20px; line-height: 1; }
  .brand--front .brand__tagline { font-size: 11px; letter-spacing: 4.6px; margin-top: 8px; }

  .brand--back { left: 56px; width: 300px; top: 143px; }
  .brand--back .brand__mark { width: 96px; height: 96px; }
  .brand--back .brand__name { font-size: 26px; letter-spacing: 2.5px; margin-top: 16px; line-height: 1; }
  .brand--back .brand__tagline { font-size: 9.5px; letter-spacing: 3.8px; margin-top: 7px; }

  .front__web {
    position: absolute; left: 0; right: 0; top: 421px;
    text-align: center; color: #fff;
    font-weight: 600; font-size: 16px; letter-spacing: 0.5px;
  }

  /* person */
  .person { position: absolute; left: 479px; top: 85px; }
  .person__name { font-weight: 800; font-size: 26px; line-height: 29px; letter-spacing: 0.5px; text-transform: uppercase; }
  .person__title { font-style: italic; font-weight: 500; font-size: 25px; line-height: 30px; color: var(--ink-soft); }

  .contacts { position: absolute; left: 483px; top: 206px; list-style: none; }
  .contacts__item {
    display: flex; align-items: center; height: 22px; margin-bottom: 19.5px;
    font-weight: 600; font-size: 16.5px; color: var(--ink-soft);
  }
  .contacts__item:nth-child(2) { margin-bottom: 18px; }
  .contacts__icon { width: 18px; height: 18px; margin-right: 13px; flex: none; fill: var(--ink-soft); }
</style>
</head>
<body>
<main class="canvas">

  <section class="card card--front" aria-label="Business card front">
    <svg class="card__shapes" viewBox="0 0 802 460" aria-hidden="true">
      <circle class="decor-ring" cx="89" cy="347" r="88" fill="none" stroke="var(--faint)" stroke-width="6"/>
      <rect x="0" y="396" width="802" height="64" fill="var(--orange)"/>
    </svg>
    <div class="brand brand--front">
      <div class="brand__mark"></div>
      <div class="brand__name">Brookvale</div>
      <div class="brand__tagline">Equipment Services</div>
    </div>
    <div class="front__web">YOURWEBDOTCOM</div>
  </section>

  <section class="card card--back" aria-label="Business card back">
    <svg class="card__shapes" viewBox="0 0 802 460" aria-hidden="true">
      <polygon points="264,0 802,0 802,35 254,35" fill="var(--orange)"/>
      <polygon points="190,430 802,430 802,460 205,460" fill="var(--ink)"/>
      <polygon points="0,403 175,403 202,460 0,460" fill="var(--orange)"/>
    </svg>
    <div class="brand brand--back">
      <div class="brand__mark"></div>
      <div class="brand__name">Brookvale</div>
      <div class="brand__tagline">Equipment Services</div>
    </div>

    <div class="person">
      <div class="person__name">Name</div>
      <div class="person__name">Sure Name</div>
      <div class="person__title">Title</div>
    </div>

    <ul class="contacts">
      <li class="contacts__item">
        <svg class="contacts__icon" viewBox="0 0 24 24"><path d="M6.6 10.8c1.4 2.8 3.8 5.1 6.6 6.6l2.2-2.2c.3-.3.7-.4 1-.2 1.1.4 2.3.6 3.6.6.6 0 1 .4 1 1V20c0 .6-.4 1-1 1C10.6 21 3 13.4 3 4c0-.6.4-1 1-1h3.5c.6 0 1 .4 1 1 0 1.3.2 2.5.6 3.6.1.3 0 .7-.2 1l-2.3 2.2z"/></svg>
        +123 456 789
      </li>
      <li class="contacts__item">
        <svg class="contacts__icon" viewBox="0 0 24 24"><path d="M2 5h20v14H2z M3.5 6.5v.4l8.5 6 8.5-6v-.4z" fill-rule="evenodd"/></svg>
        youremail
      </li>
      <li class="contacts__item">
        <svg class="contacts__icon" viewBox="0 0 24 24" fill="none" stroke="var(--ink-soft)" stroke-width="1.8"><circle cx="12" cy="12" r="9.5"/><ellipse cx="12" cy="12" rx="4.2" ry="9.5"/><path d="M2.5 12h19M4 7h16M4 17h16"/></svg>
        yourweb
      </li>
      <li class="contacts__item">
        <svg class="contacts__icon" viewBox="0 0 24 24"><path d="M12 2a7 7 0 0 0-7 7c0 5 7 13 7 13s7-8 7-13a7 7 0 0 0-7-7zm0 9.5A2.5 2.5 0 1 1 12 6.5a2.5 2.5 0 0 1 0 5z"/></svg>
        yourstreet, 1234
      </li>
    </ul>
  </section>

</main>
</body>
</html>
```